Curl Radiant through and through. Hair stylist that specializes in extensions.

I am Marisol I am a hair stylist and I would like a website designed for my hair business.

I currently book clients via my profile on trimnook.example/marisolbrantley

I need a professional website ( curlradiantthroughandthrough.example ) to display photos and prices for services offered.

I would like to have a home page with a brief bio, Image with logo and testimonials at the bottom, and a header with tab that include: menu of services, gallery,and FAQs.

On the "Services" page, I'm not interested in photos on this page. Just the name of the service, brief description, and pricing. I would also like to have, on this page, "Appointment Request" with fields that include: Name, service requested, desired time frame (morning, afternoon, evening), and contact number and email

On the "Gallery" page, I would like pictures only, but arranged and/or presented in a creative way...

Target Market(s)

Women ages 25-55 who interested in hair extension services.

Industry/Entity Type

Hair And Beauty

Coding

Number of Pages Required

5+ page

Font styles to use
Sans Serif

Requirements
Must have
• Must include tabs that include, Menu of services offered, a quick fund link to pay deposits with ease, location, contact information, photo gallery, and policy/faqs.
Nice to have
• If possible i would like to stream music with the ability to be silenced. I would like a neutral color palette tans and beige.
Should not have
• stock images

```html
<!DOCTYPE html>
<html lang="en">
<head>
<meta charset="utf-8">
<title>Our Services – Curl Radiant through and through</title>
<link rel="stylesheet" href="https://fonts.googleapis.com/css2?family=Cinzel:wght@400;700&family=Open+Sans:wght@400;600;700&display=swap">
<style>
:root{
  --tan:#cfae9f;
  --tan-dark:#b99585;
  --tan-text:#c99a86;
  --footer:#d8bfb4;
  --band:#f3f1ee;
  --line:#dcdcdc;
  --ink:#2b2b2b;
  --body:#5a5a5a;
  --price:#e0584f;
  --button:#5bb8e3;
  --white:#ffffff;
}
*{box-sizing:border-box;margin:0;padding:0}
html,body{width:1200px;height:3297px;overflow:hidden;background:var(--white)}
body{position:relative;font-family:"Open Sans",Arial,sans-serif;color:var(--body)}
.serif{font-family:"Cinzel",Georgia,serif}

/* hero */
.hero{position:absolute;left:0;top:0;width:1200px;height:396px;overflow:hidden}
.hero-photo{position:absolute;inset:0;background:linear-gradient(110deg,#3b3f47 0%,#55657a 22%,#7a6d66 45%,#a58a78 58%,#6b5a50 75%,#3c3531 100%)}
.hero-shade{position:absolute;inset:0;background:linear-gradient(180deg,rgba(0,0,0,.55) 0%,rgba(0,0,0,.25) 30%,rgba(0,0,0,.3) 100%)}
.hero-topline{position:absolute;left:0;top:0;width:100%;height:5px;background:var(--tan)}
.brand{position:absolute;left:88px;top:28px;width:240px;color:var(--white);font-weight:700;font-size:19px;line-height:24px;letter-spacing:.5px}
.contact-bar{position:absolute;right:98px;top:20px;display:flex;align-items:center;gap:12px;color:var(--white)}
.contact-bar .phone{font-family:"Cinzel",Georgia,serif;font-size:21px;margin-right:26px}
.contact-bar .login{font-family:"Cinzel",Georgia,serif;font-size:13px}
.main-nav{position:absolute;right:98px;top:71px;display:flex;gap:26px;font-family:"Cinzel",Georgia,serif;font-size:14px;color:var(--white)}
.main-nav .current{color:var(--tan)}
.hero-title{position:absolute;left:0;right:0;top:200px;text-align:center;font-family:"Cinzel",Georgia,serif;font-size:62px;letter-spacing:3px;color:var(--white)}
.hero-arrow{position:absolute;top:222px}
.hero-arrow.left{left:36px}
.hero-arrow.right{right:36px}

/* services table */
.services{position:absolute;left:99px;top:446px;width:1000px;border:1px solid var(--line)}
.table-head{display:grid;grid-template-columns:466px 198px 180px 1fr;height:51px;background:var(--tan);color:var(--white);font-family:"Cinzel",Georgia,serif;font-size:18px;letter-spacing:1px}
.table-head div{display:flex;align-items:center;justify-content:center;border-right:1px solid rgba(255,255,255,.6)}
.table-head div:last-child{border-right:0}
.service-row{display:grid;grid-template-columns:466px 198px 180px 1fr;border-top:1px solid var(--line)}
.service-row>div{border-right:1px solid var(--line);display:flex;align-items:center;justify-content:center}
.service-row>div:last-child{border-right:0}
.service-row .info{display:block;padding:24px 30px 0 35px}
.category{font-size:17px;font-weight:700;color:var(--ink);margin:8px 0 20px}
.service-name{font-size:13px;font-weight:600;color:var(--tan-text);text-transform:uppercase;margin-bottom:7px}
.desc{font-size:12px;line-height:20px;color:var(--body)}
.price{font-size:17px;color:var(--price)}
.timing{font-size:12px;color:var(--body)}
.request{width:110px;height:37px;background:var(--button);color:var(--white);font-size:12px;font-weight:700;display:flex;align-items:center;justify-content:center;border-radius:2px}

/* appointment */
.appointment{position:absolute;left:99px;top:2589px;width:1000px;height:286px;border:1px solid var(--line)}
.appointment h2{position:absolute;left:50%;top:-16px;transform:translateX(-50%);background:var(--white);padding:0 34px;font-family:"Cinzel",Georgia,serif;font-weight:400;font-size:26px;color:var(--ink);white-space:nowrap}
.field{position:absolute}
.field label,.time-label{display:block;font-size:12px;font-weight:600;color:var(--ink);margin-bottom:9px}
.field .box{width:301px;height:46px;border:1px solid var(--line)}
.time-label{position:absolute;left:354px;top:180px;margin:0}
.radio{position:absolute;top:176px;display:flex;align-items:center;gap:12px;font-size:12px;color:var(--ink)}
.radio i{width:21px;height:21px;border:1px solid #b8b8b8;border-radius:50%;display:flex;align-items:center;justify-content:center}
.radio.on i::after{content:"";width:9px;height:9px;border-radius:50%;background:#9a9a9a}
.submit{position:absolute;left:424px;top:2842px;width:352px;height:51px;background:linear-gradient(180deg,#d9c2b8,var(--tan-dark));color:var(--white);font-family:"Cinzel",Georgia,serif;font-weight:700;font-size:18px;letter-spacing:1px;display:flex;align-items:center;justify-content:center;border-radius:3px}

/* stay connected */
.connect{position:absolute;left:0;top:2939px;width:1200px;height:193px;background:var(--band);text-align:center}
.connect h3{font-family:"Cinzel",Georgia,serif;font-weight:400;font-size:26px;color:var(--ink);margin-top:34px}
.connect p{font-size:15px;color:var(--body);margin-top:10px}
.social{display:flex;justify-content:center;gap:13px;margin-top:20px}
.social span{width:31px;height:31px;border-radius:50%;background:var(--tan)}

/* footer */
.site-footer{position:absolute;left:0;top:3132px;width:1200px;height:165px;background:var(--footer);text-align:center;color:var(--white)}
.footer-brand{font-weight:700;font-size:20px;margin-top:30px}
.footer-links{font-size:12px;margin-top:18px;word-spacing:4px}
.copyright{font-size:11px;margin-top:10px}
</style>
</head>
<body>

<header class="hero">
  <div class="hero-photo" role="img" aria-label="Portrait of a client with long, freshly styled hair in a denim jacket"></div>
  <div class="hero-shade"></div>
  <div class="hero-topline"></div>
  <div class="brand">Curl Radiant through and through</div>
  <div class="contact-bar">
    <svg width="26" height="26" viewBox="0 0 26 26"><circle cx="13" cy="13" r="12" fill="none" stroke="#fff" stroke-width="1.6"/><path d="M9 7.5c.6-.5 1.3-.3 1.6.3l1 2c.3.5.1 1-.3 1.3l-.8.6c.6 1.4 1.6 2.4 3 3l.6-.8c.3-.4.9-.6 1.3-.3l2 1c.6.3.8 1 .3 1.6l-.9 1c-.6.6-1.6.7-2.4.3-2.8-1.3-4.9-3.4-6.2-6.2-.4-.8-.3-1.8.3-2.4z" fill="#fff"/></svg>
    <span class="phone">555-014-2290</span>
    <svg width="26" height="26" viewBox="0 0 26 26"><circle cx="13" cy="13" r="12" fill="#fff"/><circle cx="13" cy="10" r="4" fill="#555"/><path d="M6 20c1.5-3.5 4-5 7-5s5.5 1.5 7 5z" fill="#555"/></svg>
    <span class="login">LOGIN / SIGN UP</span>
  </div>
  <nav class="main-nav">
    <span>HOME</span><span>BIO</span><span class="current">SERVICES</span><span>PHOTO GALLERY</span><span>PAY DEPOSITS</span><span>LOCATION</span><span>CONTACT</span><span>FAQS</span>
  </nav>
  <h1 class="hero-title">OUR SERVICES</h1>
  <svg class="hero-arrow left" width="20" height="36" viewBox="0 0 20 36"><path d="M17 3L3 18l14 15" fill="none" stroke="rgba(255,255,255,.8)" stroke-width="3"/></svg>
  <svg class="hero-arrow right" width="20" height="36" viewBox="0 0 20 36"><path d="M3 3l14 15L3 33" fill="none" stroke="rgba(255,255,255,.8)" stroke-width="3"/></svg>
</header>

<section class="services">
  <div class="table-head"><div>SERVICE NAME</div><div>PRICING</div><div>TIMING</div><div></div></div>

  <div class="service-row" style="height:185px">
    <div class="info"><div class="category">BASIC SERVICES</div><div class="service-name">Shampoo and Style</div><p class="desc">Thorough shampoo and conditioning service using Lumena hair care products.<br>*$15 upcharge for closure maintenance.</p></div>
    <div><span class="price">$55 and up</span></div><div><span class="timing">90minutes</span></div><div><span class="request">REQUEST</span></div>
  </div>

  <div class="service-row" style="height:185px">
    <div class="info"><div class="category">COLOR SERVICES</div><div class="service-name">High &amp; Low Lights</div><p class="desc">Permanent coloring process using foils which includes shampoo and conditioning services. Consultation is required and relaxed hair will not be permanently colored.</p></div>
    <div><span class="price">$130 and up</span></div><div><span class="timing">120 minutes</span></div><div><span class="request">REQUEST</span></div>
  </div>

  <div class="service-row" style="height:136px">
    <div class="info"><div class="service-name">Permanent Color</div><p class="desc">Permanent coloring process which includes shampoo and conditioning services. Consultation is required and relaxed hair will not be permanently colored.</p></div>
    <div><span class="price">$125 and up</span></div><div><span class="timing">90 minutes</span></div><div><span class="request">REQUEST</span></div>
  </div>

  <div class="service-row" style="height:136px">
    <div class="info"><div class="service-name">Semi-Permanent Color</div><p class="desc">Semi-permanent, no lift process which includes shampoo and conditioning services.</p></div>
    <div><span class="price">$75 and up</span></div><div><span class="timing">90minutes</span></div><div><span class="request">REQUEST</span></div>
  </div>

  <div class="service-row" style="height:218px">
    <div class="info"><div class="category">EXTENSIONS</div><div class="service-name">Custom Extensions</div><p class="desc">Full/Partial Sew In Extensions with cut and style included. Hair must be clean and free of products upon arrival.<br>*$25 fee will be assessed if natural hair or extensions need to be shampooed.</p></div>
    <div><span class="price">$185 and up</span></div><div><span class="timing">180 minutes</span></div><div><span class="request">REQUEST</span></div>
  </div>

  <div class="service-row" style="height:156px">
    <div class="info"><div class="service-name">Extension Install</div><p class="desc">Includes the application and preparation of frontal so that it looks its most natural. Includes cut and styling.<br>*$25 fee will be assessed if natural hair or extensions need to be shampooed.</p></div>
    <div><span class="price">$300.00 and up</span></div><div><span class="timing">180 minutes</span></div><div><span class="request">REQUEST</span></div>
  </div>

  <div class="service-row" style="height:158px">
    <div class="info"><div class="service-name">Extension Coloring</div><p class="desc">Coloring 1 bundle of virgin hair using one color process.<br>*$45 per bundle for toned blondes. Extension are colored prior to the appointment. Therefore, I must receive the hair at least 7 days prior to your appointment.</p></div>
    <div><span class="price">$25.00 and up</span></div><div><span class="timing">90 minutes</span></div><div><span class="request">REQUEST</span></div>
  </div>

  <div class="service-row" style="height:180px">
    <div class="info"><div class="service-name">Extension Removal + Reinstallation</div><p class="desc">Extensions are carefully removed and hair is thoroughly cleansed and deep condition before reinstalling extensions.<br>Extension Removal $100.00 for 120 minutes<br>Extensions are carefully removed and hair is thoroughly cleansed and deep conditioned. Trim and style are included.</p></div>
    <div><span class="price">$240.00</span></div><div><span class="timing">4 hours</span></div><div><span class="request">REQUEST</span></div>
  </div>

  <div class="service-row" style="height:233px">
    <div class="info"><div class="category">STRAITENING SERVICES</div><div class="service-name">Relaxers</div><p class="desc">Veritas Relaxer system which includes a deep conditioning treatment and style of your choice.<br>Silk Press $65.00 and up for 90 minutes<br>Includes a thorough shampoo, conditioning, and silicon treatment to achieve optimal straightening of hair.</p></div>
    <div><span class="price">$75 and up</span></div><div><span class="timing">90 minutes</span></div><div><span class="request">REQUEST</span></div>
  </div>

  <div class="service-row" style="height:171px">
    <div class="info"><div class="category">UPGRADES</div><div class="service-name">Custom Haircut</div><p class="desc">Includes a thorough shampoo, conditioning, and silicon treatment to achieve optimal straightening of hair.</p></div>
    <div><span class="price">$35.00 and up</span></div><div><span class="timing">30 minutes</span></div><div><span class="request">REQUEST</span></div>
  </div>

  <div class="service-row" style="height:121px">
    <div class="info"><div class="service-name">Specialty Curls</div><p class="desc">Wand curls are typically paired with a cleansing or extension service and requires advance notice at the time of booking.</p></div>
    <div><span class="price">$25 and up</span></div><div><span class="timing">60minutes</span></div><div><span class="request">REQUEST</span></div>
  </div>

  <div class="service-row" style="height:143px">
    <div class="info"><div class="service-name">Specialty Styles</div><p class="desc">Updo styling for special events such as weddings, proms, competitions, etc.... This service is typically paired with a shampoo service.</p></div>
    <div><span class="price">$55</span></div><div><span class="timing">60 minutes</span></div><div><span class="request">REQUEST</span></div>
  </div>
</section>

<section class="appointment">
  <h2>APPOINTMENT REQUEST</h2>
  <div class="field" style="left:24px;top:50px"><label>NAME :</label><div class="box"></div></div>
  <div class="field" style="left:349px;top:50px"><label>EMAIL :</label><div class="box"></div></div>
  <div class="field" style="left:675px;top:50px"><label>PHONE NUMBER :</label><div class="box"></div></div>
  <div class="field" style="left:24px;top:138px"><label>SERVICE REQUESTED</label><div class="box"></div></div>
  <span class="time-label">DESIRED TIME FRAME :</span>
  <span class="radio on" style="left:538px"><i></i>MORNING</span>
  <span class="radio" style="left:683px"><i></i>AFTERNOON</span>
  <span class="radio" style="left:846px"><i></i>EVENING</span>
</section>
<div class="submit">SUBMIT</div>

<section class="connect">
  <h3>STAY CONNECTED</h3>
  <p>Keep up to date with changes and updates via our email newsletter.</p>
  <div class="social"><span></span><span></span><span></span><span></span><span></span></div>
</section>

<footer class="site-footer">
  <div class="footer-brand">Curl Radiant through and through</div>
  <div class="footer-links">Home | Sitemap | Contact | Login</div>
  <div class="copyright">Copyright © 2016, Curl Radiant through and through. All Right Reserved. Privacy Policy</div>
</footer>

</body>
</html>
```